Commercial Broker Profile Flyer

I need a one-page flyer created that will serve as a profile report for individual brokers within a commercial real estate firm. The flyer will include company branding, agent photo, bio, and other information. I would like to have the source file available for future editing preferably in a Publisher file format. A copy of a company brochure is included and would like to have this profile flyer similar to keep company branding consistent. Our company website is www.coltbrinwellre.com for any other questions on branding.

Target Market(s)

Professional

Industry/Entity Type

Real Estate Agent

Requirements
Must have
• One page
• Source files MUST include a .PUB file that I can update in the future
• All of the information in the uploaded "content" file
• Company branding
• Must be 8.5"x11"
Should not have
• Do not use stock photos or property photos from the attachments. I only want the broker photo and company logo.

```html
<!DOCTYPE html>
<html lang="en">
<head>
<meta charset="utf-8">
<title>Colt-Brinwell Real Estate – Broker Profile</title>
<link href="https://fonts.googleapis.com/css2?family=Lato:wght@400;700&display=swap" rel="stylesheet">
<style>
  :root {
    --green: #156b35;
    --green-dark: #0f5a2b;
    --ink: #2a2a2a;
    --white: #ffffff;
    --backdrop: #e9e9e7;
  }
  * { box-sizing: border-box; margin: 0; padding: 0; }
  html, body { width: 1200px; height: 1200px; overflow: hidden; background: var(--backdrop); }
  body { font-family: "Lato", Arial, sans-serif; color: var(--ink); }

  .flyer {
    position: absolute; left: 170px; top: 43px;
    width: 860px; height: 1113px;
    background: var(--white); overflow: hidden;
    box-shadow: 0 4px 18px rgba(0,0,0,.18);
  }
  .hero-photo {
    position: absolute; left: 0; top: 0; width: 860px; height: 460px;
    background: linear-gradient(180deg, #cdd6e0 0%, #e4ddd2 35%, #d9cfc0 60%, #6f8d55 85%, #3f6a2e 100%);
  }
  .backdrop-photo {
    position: absolute; left: 420px; top: 520px; width: 440px; height: 420px;
    background: linear-gradient(90deg, rgba(255,255,255,1) 0%, rgba(210,210,210,.55) 40%, rgba(190,190,190,.6) 100%);
  }
  .shapes { position: absolute; inset: 0; }

  .brand { position: absolute; left: 40px; top: 478px; display: flex; align-items: center; gap: 12px; color: var(--green); }
  .brand-mark { width: 64px; height: 64px; border-radius: 50%; background: var(--green); }
  .brand-name { font-size: 36px; font-weight: 400; line-height: 1; }
  .brand-sub { font-size: 16px; font-weight: 400; letter-spacing: 6px; margin-top: 4px; }

  .section-title { color: var(--green); font-weight: 700; font-size: 17px; margin-bottom: 4px; }

  .bio { position: absolute; left: 40px; top: 566px; width: 402px; }
  .bio p { font-size: 12.4px; line-height: 1.36; text-align: justify; }

  .side { position: absolute; left: 462px; top: 462px; width: 370px; }
  .side ul { list-style: none; font-size: 12.2px; line-height: 1.55; }
  .side li::before { content: "• "; color: var(--ink); }
  .clients { margin-top: 12px; }
  .clients-grid { display: grid; grid-template-columns: 140px 1fr; }

  .broker-photo {
    position: absolute; left: 545px; top: 800px; width: 240px; height: 240px;
    border-radius: 50%;
    background: radial-gradient(circle at 50% 45%, #a8a8a8 0%, #8c8c8c 60%, #777 100%);
  }

  .contact { position: absolute; left: 66px; top: 955px; color: var(--white); }
  .contact-title { font-size: 16px; font-weight: 700; text-decoration: underline; margin-bottom: 6px; }
  .contact-line { display: flex; align-items: center; gap: 8px; font-size: 18px; line-height: 1.6; }
  .contact-line small { font-size: 13px; }
  .contact-line svg { width: 14px; height: 14px; flex: none; }

  .broker-name { position: absolute; left: 545px; top: 1050px; width: 240px; text-align: center; color: var(--white); }
  .broker-name strong { display: block; font-size: 18px; font-weight: 700; white-space: nowrap; }
  .broker-name span { font-size: 14px; }
</style>
</head>
<body>
<main class="flyer">
  <div class="hero-photo" role="img" aria-label="Modern two-storey white house with palm trees and manicured hedges"></div>
  <div class="backdrop-photo" role="img" aria-label="Faded photo of a brick townhouse"></div>

  <svg class="shapes" viewBox="0 0 860 1113" aria-hidden="true">
    <path d="M0,350 C150,470 360,430 560,370 C700,330 800,305 860,295 L860,1113 L0,1113 Z" fill="#fff"/>
    <path d="M0,402 C200,492 420,432 600,382 C720,347 800,338 860,342 L860,384 C760,384 640,422 520,452 C360,492 180,502 0,446 Z" fill="#156b35"/>
    <path d="M0,372 C170,470 380,440 580,382" fill="none" stroke="#156b35" stroke-width="2"/>
    <path d="M0,918 C120,860 260,850 360,870 C480,895 560,975 860,955 L860,1113 L0,1113 Z" fill="#156b35"/>
    <path d="M0,898 C140,842 260,845 340,862" fill="none" stroke="#156b35" stroke-width="3"/>
    <path d="M10,940 C120,885 250,875 340,888" fill="none" stroke="#fff" stroke-width="5"/>
    <circle cx="665" cy="920" r="136" fill="#156b35"/>
    <circle cx="665" cy="920" r="128" fill="#fff"/>
  </svg>

  <div class="broker-photo" role="img" aria-label="Portrait of the broker"></div>

  <div class="brand">
    <div class="brand-mark"></div>
    <div>
      <div class="brand-name">Colt-Brinwell</div>
      <div class="brand-sub">REAL ESTATE</div>
    </div>
  </div>

  <section class="bio">
    <h2 class="section-title">Bio</h2>
    <p>Nolan began his real estate career in 2005 and has completed $75+ million in transactions representing sellers and buyers of commercial real estate, providing tenant representation, and leasing of retail and office properties. Prior to beginning his real estate career, Nolan served over five years in the Army Reserves and attended Eastfield State University.</p>
    <p>Nolan has earned the prestigious Chartered Commercial Property Advisor (CCPA) designation as well as the Accredited Leasing Professional (ALP) designation. Nolan is a member of the International Council of Retail Centers (ICRC), the State and Millbrook Realtor Association, the Millbrook-Harlan County Chamber of Commerce, and serves on the board of directors for the Regional CCPA Chapter, the Sandridge Youth Association, and the Tallpine Realtors Association. Nolan is a licensed real estate broker in NC and SC.</p>
  </section>

  <section class="side">
    <h2 class="section-title">Professional Affiliations</h2>
    <ul>
      <li>Chartered Commercial Property Advisor (designee)</li>
      <li>International Council of Retail Centers</li>
      <li>Tallpine Realtors Association</li>
      <li>State Realtors Commercial Forms Committee</li>
    </ul>
    <div class="clients">
      <h2 class="section-title">Clients Served</h2>
      <div class="clients-grid">
        <ul>
          <li>Brightbird Chicken</li>
          <li>Four Friends Grill</li>
          <li>Team Trims</li>
          <li>Value Tread Tires</li>
          <li>LittleBakes</li>
        </ul>
        <ul>
          <li>Harbor Home Health</li>
          <li>Kinpath Services</li>
          <li>Main Street Media</li>
          <li>Crestline Beverage Group</li>
        </ul>
      </div>
    </div>
  </section>

  <section class="contact">
    <h2 class="contact-title">Contact Information</h2>
    <div class="contact-line">
      <svg viewBox="0 0 16 16"><path d="M3 1l3 3-1.5 2c1 2 2.5 3.5 4.5 4.5L11 9l3 3-2 2C6 13 3 10 1 4z" fill="#fff"/></svg>
      <span>(336) 555-0142 ext. 314 <small>(Office Phone)</small></span>
    </div>
    <div class="contact-line">
      <svg viewBox="0 0 16 16"><path d="M3 1l3 3-1.5 2c1 2 2.5 3.5 4.5 4.5L11 9l3 3-2 2C6 13 3 10 1 4z" fill="#fff"/></svg>
      <span>(336) 555-0187 <small>(Cell Phone)</small></span>
    </div>
    <div class="contact-line">
      <svg viewBox="0 0 16 16"><rect x="1" y="3" width="14" height="10" fill="#fff"/><path d="M1 3l7 6 7-6" fill="none" stroke="#156b35" stroke-width="1.5"/></svg>
      <span>nolan@coltbrinwellre.com</span>
    </div>
    <div class="contact-line">
      <svg viewBox="0 0 16 16"><circle cx="8" cy="8" r="6.5" fill="none" stroke="#fff" stroke-width="1.5"/><path d="M1.5 8h13M8 1.5c-3 3.5-3 9.5 0 13M8 1.5c3 3.5 3 9.5 0 13" fill="none" stroke="#fff" stroke-width="1.2"/></svg>
      <span>www.coltbrinwellre.com</span>
    </div>
  </section>

  <div class="broker-name">
    <strong>T. Nolan Brinwell, CCPA, ALP</strong>
    <span>Principal / Broker in Charge</span>
  </div>
</main>
</body>
</html>
```